Pet Shop Website

website will need to have the following features:
• Photo Galleries of each species (Dogs, Cats, Birds, Fish, Reptiles, Rabbits) in a light box popup
o Each species may have several different categories for example:
 Fish
• Marine fish
• Fresh water
• tropical
• Cichlid
• Information Fact sheets of each species – Downloaded as a pdf which can be either
o Care Sheets
o Training Sheets
• Members Area
o Username (Email Address) & Password login
o New signups
o Exclusive Member Deals
o Newsletter options

The front page must be very simple (for example lumavest.com.au) contain the following:
• Product of the week - which can be purchased online
o Short details
o Cost
• Pet Club Sign up picture
• Animal of the week/month
• Contact Phone Number and addresses of the stores
• A jQuery slideshow (Images could include stores, pets etc…)
The main page MUST keep simple. We do not want it cluttered.

Inner Page
The animals / reptile page will need to have:
• Short description of the species
• Photo Galleries
• A list of what is in stock and the list needs to clearly be sorted by each store (Use of Tabs maybe).
• Facts sheets / Info sheets
The type of website ideas (not the type of look that we are necessary after) is and the sort of content that we want to offer are as follows:

http://www.scalenook.com.au/
http://www.brindlecovepaws.com.au/
http://www.thefurrowden.com.au
http://www.tailtown.net.au

Colour in the new website:
Blue
Red
Grey
Yellow

Original site:

http://www.critterglow.com.au
Updates

Hi Guys,

We had feedback from the client and they would like to see a few dark designs.

Thanks                                   

Reason: We would like to reopen this contest back up for a further week

Target Market(s)

Targeting animal lovers

Industry/Entity Type

Store

Requirements
Should not have
• Alter the logo in anyway

```html
<!DOCTYPE html>
<html lang="en">
<head>
<meta charset="utf-8">
<title>Critter Glow – Home</title>
<link href="https://fonts.googleapis.com/css2?family=Merriweather:wght@400;700&family=Noto+Serif:ital,wght@0,400;1,400;1,700&family=Arimo:ital,wght@0,400;1,400&family=Roboto+Condensed&display=swap" rel="stylesheet">
<style>
:root{
  --page-bg:#f4f3f3;
  --panel:#f6f5f5;
  --teal:#2fa3b3;
  --blue-band:#1f6fb5;
  --nav-red:#a3101c;
  --head-red:#b31c10;
  --ink:#2d2d2d;
  --grey-text:#777;
  --quote-bg:#e1e1e1;
  --frame-blue:#2a8fdf;
  --yellow:#e2c00e;
  --yellow-line:#e0b600;
  --green-top:#8cc152;
  --green-bot:#4c8a1f;
}
*{margin:0;padding:0;box-sizing:border-box}
html,body{width:779px;height:1200px;overflow:hidden}
body{background:var(--page-bg);position:relative;font-family:"Arimo",Arial,sans-serif;color:var(--ink)}
.abs{position:absolute}
.top-line{left:0;top:0;width:779px;height:3px;background:var(--teal)}
.side-band{top:7px;height:176px;background:linear-gradient(135deg,#2b7cc2,#1a5fa3)}
.side-band.left{left:0;width:39px}
.side-band.right{right:0;width:40px}
.band-line{left:0;top:184px;width:779px;height:4px;background:var(--teal)}
.panel{left:38px;top:7px;width:701px;height:1155px;background:var(--panel);box-shadow:0 6px 10px rgba(0,0,0,.35)}
.brand{left:58px;top:38px;display:flex;align-items:center;gap:8px;font-family:"Noto Serif",serif;font-size:22px;color:var(--nav-red)}
.brand-dot{width:18px;height:18px;border-radius:50%;background:var(--blue-band)}
.nav-tab{left:311px;top:4px;width:57px;height:80px;background:#cfcdce;border-radius:0 0 6px 6px}
.nav a{position:absolute;top:56px;font-family:"Noto Serif",serif;font-style:italic;font-size:13px;color:var(--nav-red);text-decoration:none}
.nav a.active{text-decoration:underline}
.nav .caret{display:inline-block;margin-left:6px;border:3px solid transparent;border-top:4px solid var(--frame-blue);vertical-align:middle}
.hero-top{left:38px;top:109px;width:701px;height:4px;background:var(--teal)}
.hero{left:38px;top:113px;width:701px;height:319px;background:linear-gradient(90deg,#e8e2da 0%,#b48a60 30%,#9a7345 62%,#8c6a3c 100%)}
.hero-bottom{left:38px;top:432px;width:701px;height:6px;background:#1e8a9a}
.hero-title{left:514px;top:142px;width:210px;font-family:"Noto Serif",serif;font-style:italic;font-size:23px;line-height:32px;color:#e6d9bf}
.hero-sub{left:514px;top:243px;width:200px;font-family:"Noto Serif",serif;font-style:italic;font-size:15.5px;line-height:20px;color:#fff}
.dots{left:578px;top:390px;display:flex;gap:8px}
.dots span{width:10px;height:10px;border-radius:50%;background:#fff}
.dots span.on{background:#f3c316}
.welcome-title{left:64px;top:468px;font-family:"Merriweather",serif;font-size:20px;color:var(--ink)}
.welcome-sub{left:64px;top:492px;font-family:"Noto Serif",serif;font-style:italic;font-weight:700;font-size:13.5px;color:var(--teal)}
.club-photo{left:65px;top:532px;width:178px;height:130px;background:#d8d8d8;padding:4px}
.club-photo div{width:100%;height:100%;background:linear-gradient(135deg,#5b6066,#8e939a 50%,#3d4146)}
.intro{left:257px;top:530px;width:270px;font-size:7.8px;line-height:15px;color:var(--grey-text)}
.intro-links{left:257px;top:602px;list-style:none;font-size:7.8px;line-height:15.2px}
.intro-links li::before{content:"";display:inline-block;width:4px;height:4px;background:var(--teal);margin-right:7px;vertical-align:middle}
.intro-links a{color:var(--ink)}
.quote{left:557px;top:473px;width:158px;height:165px;background:var(--quote-bg);border-top:4px solid var(--teal);font-family:"Noto Serif",serif;font-style:italic;font-weight:700;font-size:13.5px;line-height:20.5px;color:#333;text-align:center;padding:36px 10px 0}
.quote-tip{left:629px;top:638px;border:6px solid transparent;border-top:6px solid var(--quote-bg)}
.quote-by{left:557px;top:638px;width:158px;height:30px;background:#efefef;font-size:9px;text-align:center;padding-top:12px;color:#444}
.divider{left:64px;top:686px;width:650px;height:1px;background:#d4d4d4}
.feature{left:38px;top:689px;width:701px;height:246px;background:linear-gradient(180deg,var(--panel) 0%,#f1e6a4 25%,var(--yellow) 55%,#f0e49e 85%,var(--panel) 100%)}
.feature-rule{left:374px;top:692px;width:2px;height:237px;background:var(--yellow-line)}
.feature-title{font-family:"Noto Serif",serif;font-style:italic;font-size:20px;color:var(--head-red)}
.photo-frame{border:2px solid var(--frame-blue);background:#fff}
.lizard{left:78px;top:732px;width:213px;height:155px}
.lizard div{margin:8px;height:135px;background:radial-gradient(ellipse at center,#7f9a4c 0%,#b7c78e 45%,#fff 75%)}
.bird{left:437px;top:727px;width:214px;height:155px;background:linear-gradient(160deg,#86b53c,#5d8f2a 55%,#7a6e55)}
.price{left:77px;top:898px;font-family:"Roboto Condensed",sans-serif;font-size:15px;color:var(--teal)}
.price small{font-family:"Arimo",sans-serif;font-size:8.5px;color:#666;margin-left:10px}
.btn{display:flex;align-items:center;gap:8px;height:21px;padding-left:6px;border-radius:3px;background:linear-gradient(180deg,var(--green-top),var(--green-bot));font-family:"Noto Serif",serif;font-style:italic;font-size:8.5px;color:#fff;box-shadow:0 1px 2px rgba(0,0,0,.3)}
.btn i{width:12px;height:12px;border-radius:50%;background:#fff;display:flex;align-items:center;justify-content:center}
.btn i::after{content:"";border:3px solid transparent;border-left:4px solid #444;margin-left:3px}
.buy{left:246px;top:900px;width:74px}
.read{left:616px;top:896px;width:75px}
.month-text{left:439px;top:888px;width:160px;font-size:9.5px;line-height:12.5px;color:var(--teal);text-align:justify}
.foot-rule{left:64px;top:936px;width:650px;height:3px;background:#dcdcdc}
.foot-col h4{font-family:"Noto Serif",serif;font-style:italic;font-weight:700;font-size:9.5px;color:#333;margin-bottom:12px}
.foot-col ul{list-style:none;font-size:8.3px;color:var(--grey-text);line-height:20.5px}
.foot-col li::before{content:"";display:inline-block;width:3px;height:3px;background:var(--teal);margin-right:5px;vertical-align:middle}
.foot-col li.link{color:var(--teal)}
.location p{font-size:7.8px;line-height:12px;color:#555}
.location .label{color:var(--teal)}
.news-input{width:157px;height:21px;border:1px solid #ddd;background:#fff;font-size:8.5px;color:#777;padding:5px 6px;position:relative}
.news-input span{position:absolute;right:0;top:2px;width:17px;height:15px;background:#eee;display:flex;align-items:center;justify-content:center}
.news-input span::after{content:"";border:3px solid transparent;border-left:4px solid #999;margin-left:3px}
.copy{left:57px;top:1139px;font-style:italic;font-size:9px;color:#444}
</style>
</head>
<body>
<div class="abs top-line"></div>
<div class="abs side-band left" role="img" aria-label="Blue diagonal-stripe side band"></div>
<div class="abs side-band right" role="img" aria-label="Blue diagonal-stripe side band"></div>
<div class="abs band-line"></div>

<div class="abs panel"></div>

<header>
  <div class="abs brand"><span class="brand-dot"></span>Critter Glow</div>
  <div class="abs nav-tab"></div>
  <nav class="nav">
    <a class="active" href="#" style="left:322px">Home</a>
    <a href="#" style="left:388px">About Us</a>
    <a href="#" style="left:472px">Pets<span class="caret"></span></a>
    <a href="#" style="left:531px">Photogallery</a>
    <a href="#" style="left:619px">Contact Us</a>
  </nav>
</header>

<section class="slideshow">
  <div class="abs hero-top"></div>
  <div class="abs hero" role="img" aria-label="Slideshow photo of a brown lop-eared rabbit on a soft blanket, fading into a warm brown panel"></div>
  <div class="abs hero-bottom"></div>
  <h2 class="abs hero-title">Express Help for Your Pet!</h2>
  <p class="abs hero-sub">Lorem ipsum dolor sit amet, consectetuer adipiscing elit,</p>
  <div class="abs dots"><span class="on"></span><span></span><span></span><span></span><span></span></div>
</section>

<section class="club">
  <h1 class="abs welcome-title">Welcome to Our Club</h1>
  <p class="abs welcome-sub">Lorem ipsum dolor sit amet, consectetuer adipiscing, sed diam</p>
  <div class="abs club-photo"><div role="img" aria-label="Photo of a grey tabby cat"></div></div>
  <p class="abs intro">Lorem ipsum dolor sit amet, consectetuer adipiscing elit, sed diam nonummy nibh euismod tincidunt ut laoreet dolore magna aliquam erat volutpat. Ut wisi enim ad minim veniam, quis nostrud exerci tation ullamcorper suscipit lobortis nisl ut aliquip ex ea commodo consequat.</p>
  <ul class="abs intro-links">
    <li><a href="#">Lorem ipsum dolor sit amet,</a></li>
    <li><a href="#">consectetuer adipiscing elit, sed diam</a></li>
    <li><a href="#">nonummy nibh euismod tincidunt ut</a></li>
    <li><a href="#">laoreet dolore.</a></li>
  </ul>
  <blockquote class="abs quote">“ Lorem ipsum dolor sit amet, lore consectetuer adipiscing nonmmy nibh.”</blockquote>
  <div class="abs quote-by">Noel Barrow</div>
  <div class="abs quote-tip"></div>
  <div class="abs divider"></div>
</section>

<section class="featured">
  <div class="abs feature"></div>
  <div class="abs feature-rule"></div>

  <h3 class="abs feature-title" style="left:77px;top:694px">Animal of the Week</h3>
  <div class="abs photo-frame lizard"><div role="img" aria-label="Photo of a green water dragon lizard"></div></div>
  <p class="abs price">Price - $66<small>(Online Purchased)</small></p>
  <a class="abs btn buy" href="#"><i></i>Buy Now</a>

  <h3 class="abs feature-title" style="left:439px;top:689px">Animal of the Month</h3>
  <div class="abs photo-frame bird" role="img" aria-label="Photo of a red cardinal bird perched on a log"></div>
  <p class="abs month-text">Lorem ipsum dolor sit amet, consectetur adipiscing elit. Cras bibendum ligula id.</p>
  <a class="abs btn read" href="#"><i></i>Read More</a>
</section>

<footer>
  <div class="abs foot-rule"></div>
  <div class="abs foot-col" style="left:63px;top:964px">
    <h4>Quick Links</h4>
    <ul><li class="link">About</li><li>Pets</li><li>Photogallery</li><li>Contacts</li></ul>
  </div>
  <div class="abs foot-col" style="left:173px;top:964px">
    <h4>Popular</h4>
    <ul><li>Lorem ipsum dolor</li><li>Sit amet</li><li>Consectetuer</li><li>Adipiscing elit sed</li><li>Diam nonummy</li></ul>
  </div>
  <div class="abs foot-col" style="left:282px;top:964px">
    <h4>Social Pages</h4>
    <ul><li>Chirpline</li><li>Friendwall</li><li>Circlenet</li><li>RSS</li></ul>
  </div>
  <div class="abs foot-col location" style="left:389px;top:964px">
    <h4 style="margin-left:3px">Our Location</h4>
    <p>Unit 4 / 22 Harbour Lane<br>COOGEE VALE, W.A 6170</p>
    <p style="margin-top:12px"><span class="label">Phone:</span> (08) 9555 0142<br><span class="label">Fax:</span> (08) 9555 0148</p>
  </div>
  <div class="abs foot-col" style="left:556px;top:964px">
    <h4>Newsletter</h4>
    <div class="news-input">Enter Email:<span></span></div>
  </div>
  <p class="abs copy">Critter Glow (c) 2013-2014 . Privacy Policy</p>
</footer>
</body>
</html>
```